Letterhead for New Orthopaedic Surgery Practice

My husband and I are starting our own practice named RB Spine & Vitality Center. We would like to create a nice simple but high class letterhead that doesn't use too much solid color ink when printing. I like the colors dark blue, gold, yellow. Open to other suggestions. We will need to list him and I both on the top of the letterhead. Here is the important information:
Lucinda Perrow, M.D. - Hand and Upper Extremity Surgery
Abena Quist, M.D. - Hip & Knee Replacement/General Orthopaedic Surgery
Location: 18735 North Harlow Pkwy
Linden Shores, FL 33488
Phone: 954-218-4650
Fax: 954-582-1346
Email: info@myrbspine.com

The only thing is that the phone and fax numbers will change once we get into our space. I just want to get the design started. I am including several documents which are my previous practice letterhead, my current procedure room letterhead, and our new Logo. The other letterheads are just for examples but please think outside of the box! We would love to see some great designs.

Colors
0054AA
0677BA
7BADD7
CADEEF
E8F1F8
0094D4
00A9DD
6FCCEA
C7EBF8
E9F6FB

Requirements
Must have
• class, elegance, luxury

```html
<!DOCTYPE html>
<html lang="en">
<head>
<meta charset="utf-8">
<title>RB Spine &amp; Vitality Center — Letterhead</title>
<link rel="stylesheet" href="https://fonts.googleapis.com/css2?family=Mulish:wght@400;600;700&display=swap">
<style>
  :root {
    --navy: #0054AA;
    --sky: #00A9DD;
    --ink: #2a3550;
    --rule: #CADEEF;
    --mist: #E8F1F8;
    --backdrop: #EEEFF1;
    --paper: #FFFFFF;
  }
  * { box-sizing: border-box; margin: 0; padding: 0; }
  html, body {
    width: 1102px;
    height: 1200px;
    overflow: hidden;
    background: var(--backdrop);
    font-family: "Mulish", "Helvetica Neue", Arial, sans-serif;
  }
  .letterhead {
    position: absolute;
    left: 141px;
    top: 20px;
    width: 820px;
    height: 1160px;
    background: var(--paper);
    overflow: hidden;
  }
  .brand {
    position: absolute;
    left: 70px;
    top: 76px;
    display: flex;
    align-items: center;
    gap: 14px;
  }
  .brand-square {
    width: 40px;
    height: 40px;
    background: var(--navy);
  }
  .brand-name {
    font-weight: 700;
    font-size: 19px;
    line-height: 1.15;
    color: var(--navy);
    width: 170px;
  }
  .physicians {
    position: absolute;
    right: 70px;
    top: 72px;
    text-align: right;
  }
  .physician + .physician { margin-top: 9px; }
  .physician-name {
    font-weight: 700;
    font-size: 12px;
    color: var(--sky);
    letter-spacing: 0.2px;
  }
  .physician-specialty {
    font-size: 8.5px;
    color: var(--ink);
    margin-top: 3px;
  }
  .footer-art {
    position: absolute;
    left: 400px;
    top: 950px;
    width: 440px;
    height: 230px;
    background: radial-gradient(ellipse 50% 50% at 55% 60%, var(--mist) 0%, rgba(232,241,248,0.6) 55%, rgba(255,255,255,0) 100%);
  }
  .footer-rule {
    position: absolute;
    left: 70px;
    top: 1056px;
    width: 677px;
    height: 1px;
    background: var(--rule);
  }
  .footer-block {
    position: absolute;
    top: 1072px;
    font-size: 9px;
    line-height: 1.55;
    color: var(--navy);
  }
  .footer-address { left: 122px; }
  .footer-numbers { left: 377px; }
  .footer-email { left: 607px; top: 1078px; }
  .footer-label { font-weight: 700; }
</style>
</head>
<body>
  <main class="letterhead">
    <header>
      <div class="brand">
        <div class="brand-square"></div>
        <div class="brand-name">RB Spine &amp; Vitality Center</div>
      </div>
      <div class="physicians">
        <div class="physician">
          <div class="physician-name">Lucinda Perrow, M.D.</div>
          <div class="physician-specialty">Hand and Upper Extremity Surgery</div>
        </div>
        <div class="physician">
          <div class="physician-name">Abena Quist, M.D.</div>
          <div class="physician-specialty">Hip &amp; Knee Replacement/General Orthopaedic Surgery</div>
        </div>
      </div>
    </header>

    <div class="footer-art" role="img" aria-label="Faint pale-blue leafy branch decoration"></div>

    <footer>
      <div class="footer-rule"></div>
      <div class="footer-block footer-address">
        18735 North Harlow Pkwy<br>
        Linden Shores, FL 33488
      </div>
      <div class="footer-block footer-numbers">
        <span class="footer-label">FAX:</span> 954-582-1346<br>
        <span class="footer-label">Phone:</span> 954-218-4650
      </div>
      <div class="footer-block footer-email">info@myrbspine.com</div>
    </footer>
  </main>
</body>
</html>
```